Create a Magazine Ad for an asbestos law firm

we need an 8 X 13 ad to be on the back of a magazine cover. We have the text Attached and want a similar look and feel to our website : www.harborvale-claims.example. The ad should be targeted to white males 55 years or older who are conservative and worked in industry or industrial plants. The main offer is a free case review and trying to get them to call the telephone number.

Target Market(s)

White collar men who worked in industrial plants. Age 55 years or older.

Industry/Entity Type

Legal

Requirements
Must have
• Pictures of white middle class conservative man or man and woman
Nice to have
• look at www.harborvale-claims.example to an. idea of what we are looking for

```html
<!DOCTYPE html>
<html lang="en">
<head>
<meta charset="utf-8">
<title>Mesothelioma Compensation – Magazine Ad</title>
<link rel="stylesheet" href="https://fonts.googleapis.com/css2?family=Oswald:wght@500;600&family=Open+Sans:wght@400;600;700&display=swap">
<style>
  :root {
    --navy: #1f3651;
    --ink: #2a2f36;
    --paper: #ffffff;
    --grass-dark: #5c7a3e;
    --grass-light: #a9bf7a;
    --sky: #dfe6de;
  }
  * { box-sizing: border-box; margin: 0; padding: 0; }
  html, body { width: 874px; height: 1200px; overflow: hidden; background: var(--paper); }
  .ad {
    position: relative; width: 874px; height: 1200px;
    font-family: "Open Sans", Arial, sans-serif; color: var(--ink);
  }
  .hero-photo {
    position: absolute; left: 0; top: 0; width: 874px; height: 585px;
    background: linear-gradient(180deg, var(--sky) 0%, #c9d4b8 30%, var(--grass-light) 55%, var(--grass-dark) 100%);
  }
  .left-col {
    position: absolute; left: 40px; top: 622px; width: 360px;
    display: flex; flex-direction: column;
  }
  .headline {
    font-family: "Oswald", "Arial Narrow", sans-serif; font-weight: 600;
    font-size: 42px; line-height: 1.24; color: var(--navy); text-transform: uppercase;
    width: 380px; white-space: nowrap;
  }
  .firm { margin-top: 12px; font-size: 13px; line-height: 1.35; }
  .results { margin-top: 10px; font-size: 12.5px; line-height: 1.32; width: 100%; border-collapse: collapse; }
  .results td { padding: 0; }
  .results td:last-child { text-align: right; }
  .cta {
    margin-top: 14px; width: 356px;
    background: var(--navy); color: #fff; padding: 10px 14px;
    font-size: 12.5px; line-height: 1.32;
  }
  .right-col { position: absolute; left: 420px; top: 612px; width: 420px; font-size: 14px; line-height: 1.42; }
  .right-col p { margin-bottom: 8px; }
  .right-col strong { font-weight: 700; }
  .right-col ul { margin: 0 0 10px 22px; }
  .right-col h2 { font-size: 14.5px; font-weight: 700; color: var(--navy); margin: 10px 0 6px; }
</style>
</head>
<body>
<div class="ad">
  <div class="hero-photo" role="img" aria-label="Older couple meditating together on mats on a sunny park lawn"></div>

  <div class="left-col">
    <h1 class="headline">Diagnosed with<br>Mesothelioma,<br>You could be owed<br>Compensation</h1>
    <p class="firm">Whitcombe &amp; Arlen, LLP, Daniel Whitcombe,<br>Port Calder, TX</p>
    <table class="results">
      <tr><td>Exposed through heavy duty vehicles</td><td>$6,742,500</td></tr>
      <tr><td>Exposed through general contracting</td><td>$6,033,510</td></tr>
      <tr><td>Exposed through boat repair</td><td>$5,939,010</td></tr>
      <tr><td>Exposed through navy service</td><td>$3,921,750</td></tr>
      <tr><td>Exposed through navy service</td><td>$3,600,450</td></tr>
      <tr><td>Exposed from Talcum Baby Powder</td><td>$2,665,000</td></tr>
    </table>
    <div class="cta">
      Find out if you're Eligible, for FREE, in Minutes<br>
      We'll evaluate your situation and tell you what your case could be worth.<br>
      Get your Free evaluation now!<br>
      CALL 1-XXX-XXXX (good number)
    </div>
  </div>

  <div class="right-col">
    <p>It's very likely you developed this disease through <strong>asbestos exposure. Mesothelioma patients are getting multi-million dollar settlements, decades later, from:</strong></p>
    <ul>
      <li>Exposure to asbestos products,</li>
      <li>Ex-employers, or</li>
      <li>Talcum baby powder companies.</li>
    </ul>
    <p><strong>We can help you find out if you qualify for a case in minutes.</strong></p>
    <ul>
      <li>We'll analyze your situation at no cost</li>
      <li>Determine how much compensation you could be entitled too</li>
      <li>Give you the next steps to get what you're owed</li>
    </ul>
    <h2>$30 Billion is Available in Trust for Mesothelioma Patients</h2>
    <p>Tradesmen in many industries were negligently exposed to asbestos materials well into the 1990s. Whether you developed Mesothelioma yourself due to asbestos exposure or you're the surviving family of a lost loved one you could be entitled to significant compensation.</p>
    <h2>How much Money Can People Receive from a Mesothelioma Case?</h2>
    <p>Depending on where you were exposed and a few other factors, you can get a settlement from 6 to 7 figures. Here are a few examples of Mesothelioma Settlements received by our clients. These figures are the total compensation after all attorney fees and expenses are deducted.</p>
  </div>
</div>
</body>
</html>
```